Business Card For Video Production Company

Please NOTE: I've added some info to the must haves that I should have included at the start. Thank you.

I need a business card design for my video production company based in Orlando called Caldera Film Works. Our work consists of web video marketing (web videos), training videos, sales videos, conference and seminar video production...basically a lot of corporate based work.

We work with successful small businesses, not-for-profits and some Fortune 500 type groups. We bring a lot of knowledge, experience and attention to detail to every project.

I'd like something that communicates strength, confidence, integrity, as well as creative vision. I want to stay away from the standard icons of the media and film industry. I'd like to emphasize the colors of my logo, and also the colors of my website which has a white background. Simple is good.

Our budgets are moderate...generally $1500 to $5000.

www.calderafilm.tv

PS...We don't do weddings or recitals, or that type of production.
Updates

I want to thank all the designers for your updates. There's way too many to be able to give feedback on for all. I hope you understand that. But wow…there are so many great designs everyone has offered. I can't thank you enough…each and everyone. I hope to make my decision soon. I'm not accepting anymore designs from new designers. Brent-

Target Market(s)

Successful small businesses, marketing directors, corporate communication directors, training and human resources professionals. forward thinking not-for profits. Since my company is based in Central Florida, most of my work comes from this area too.

Industry/Entity Type

Marketing

Requirements
Must have
• website address, www.calderafilm.tv
phone number, 407-552-9031
email address, brent@calderafilm.tv

Title
Brent Caldera
Owner/Creative Director

I'd like to have a single line that goes across illustrating our services, maybe separated with bullet points:

Marketing Videos, Corporate Videos, Conference & Seminar Video Production
Should not have
• No film or video icons.
No need to pull language or copy from my website.

```html
<!DOCTYPE html>
<html lang="en">
<head>
<meta charset="utf-8">
<title>Caldera Film Works — Business Card</title>
<link rel="stylesheet" href="https://fonts.googleapis.com/css2?family=Open+Sans:wght@400;600;700;800&display=swap">
<style>
  :root {
    --bg: #e9eaec;
    --card-white: #fafafa;
    --ink: #3a3d42;
    --ink-soft: #55595f;
    --rule: #9a9da2;
    --blue: #1f8fe0;
    --blue-deep: #0a5fae;
    --blue-mid: #137bd0;
    --blue-light: #4fb8f5;
    --white: #ffffff;
  }
  * { margin: 0; padding: 0; box-sizing: border-box; }
  html, body {
    width: 1200px; height: 1024px; overflow: hidden;
    background: var(--bg);
    font-family: "Open Sans", Arial, sans-serif;
  }
  .stage {
    width: 1200px; height: 1024px;
    display: flex; flex-direction: column;
    align-items: center; justify-content: center; gap: 40px;
  }
  .card {
    position: relative;
    width: 800px; height: 457px;
    border-radius: 4px;
    overflow: hidden;
    box-shadow: 0 6px 18px rgba(0,0,0,.18);
  }

  /* Front */
  .card-front { background: var(--card-white); }
  .brand {
    position: absolute; left: 56px; top: 52px;
    display: flex; align-items: center; gap: 18px;
  }
  .brand-mark {
    width: 64px; height: 64px; background: var(--blue);
  }
  .brand-name {
    font-size: 44px; font-weight: 800; color: var(--ink);
    letter-spacing: -0.5px; line-height: 1;
  }
  .rule {
    position: absolute; left: 56px; right: 56px; height: 1px;
    background: var(--rule);
  }
  .rule-top { top: 150px; }
  .rule-bottom { top: 340px; }
  .person {
    position: absolute; left: 330px; top: 172px;
  }
  .person-name {
    font-size: 30px; font-weight: 600; color: var(--blue); line-height: 1.15;
  }
  .person-title {
    font-size: 17px; font-weight: 700; color: var(--ink); margin-top: 2px;
  }
  .contacts {
    position: absolute; left: 56px; right: 56px; top: 282px;
    display: flex; justify-content: space-between; align-items: center;
    font-size: 17px; color: var(--ink-soft);
  }
  .contact { display: flex; align-items: center; gap: 8px; }
  .contact svg { width: 20px; height: 20px; flex: none; }
  .services {
    position: absolute; left: 56px; right: 56px; top: 370px;
    height: 40px; border-radius: 10px;
    background: var(--blue);
    color: var(--white);
    font-size: 17px; font-weight: 400;
    display: flex; align-items: center; justify-content: center;
  }

  /* Back */
  .card-back { background: var(--blue-deep); }
  .back-artwork {
    position: absolute; inset: 0;
    background: linear-gradient(135deg, var(--blue-deep) 0%, var(--blue-mid) 55%, var(--blue-light) 100%);
  }
  .back-brand {
    position: absolute; left: 70px; top: 150px;
    display: flex; align-items: center; gap: 18px;
  }
  .back-brand .brand-mark { background: var(--white); width: 60px; height: 60px; }
  .back-brand .brand-name { color: var(--white); font-size: 46px; }
</style>
</head>
<body>
<main class="stage">

  <section class="card card-front" aria-label="Business card front">
    <div class="brand">
      <div class="brand-mark"></div>
      <div class="brand-name">Caldera Film Works</div>
    </div>
    <div class="rule rule-top"></div>

    <div class="person">
      <div class="person-name">Brent Caldera</div>
      <div class="person-title">Owner/Creative Director</div>
    </div>

    <div class="contacts">
      <div class="contact">
        <svg viewBox="0 0 20 20" aria-hidden="true">
          <circle cx="10" cy="10" r="9" fill="var(--blue)"/>
          <g fill="none" stroke="#fff" stroke-width="1.2">
            <circle cx="10" cy="10" r="6"/>
            <ellipse cx="10" cy="10" rx="2.6" ry="6"/>
            <line x1="4" y1="10" x2="16" y2="10"/>
          </g>
        </svg>
        <span>www.calderafilm.tv</span>
      </div>
      <div class="contact">
        <svg viewBox="0 0 20 20" aria-hidden="true">
          <path d="M5 2.5c1 0 2.6 3.3 2.6 4.2 0 .9-1.6 1.5-1.6 2.4 0 1.3 3 4.4 4.4 4.4.9 0 1.5-1.6 2.4-1.6.9 0 4.2 1.6 4.2 2.6 0 1.4-1.8 3-3.4 3C8.4 17.5 2.5 11.6 2.5 6c0-1.600 1.3-3.5 2.5-3.5z" fill="var(--blue)"/>
        </svg>
        <span>407-552-9031</span>
      </div>
      <div class="contact">
        <svg viewBox="0 0 20 20" aria-hidden="true">
          <circle cx="10" cy="10" r="9" fill="var(--blue)"/>
          <rect x="5" y="6.5" width="10" height="7" fill="none" stroke="#fff" stroke-width="1.2"/>
          <polyline points="5,6.5 10,10.5 15,6.5" fill="none" stroke="#fff" stroke-width="1.2"/>
        </svg>
        <span>brent@calderafilm.tv</span>
      </div>
    </div>
    <div class="rule rule-bottom"></div>

    <div class="services">Marketing Videos, Corporate Videos, Conference &amp; Seminar Video Production</div>
  </section>

  <section class="card card-back" aria-label="Business card back">
    <div class="back-artwork" role="img" aria-label="Decorative geometric background artwork in blue tones"></div>
    <div class="back-brand">
      <div class="brand-mark"></div>
      <div class="brand-name">Caldera Film Works</div>
    </div>
  </section>

</main>
</body>
</html>
```